Business Card design for shipping company 'FERNHOLT INTERNATIONAL LTD'

Classic / traditional business card in black Garamond / Times New Roman or similar text for a shipping / marine transport company, containing the following information:

QUOTE

FERNHOLT INTERNATIONAL LTD

MARTIN QUESTEDGE FICS

T: +44 7902 615370
E: cargo@fernholt-example.com

UNQUOTE

Target Market(s)

Marine / Shipping industry

Contact Information for Business Card

FERNHOLT INTERNATIONAL LTD MARTIN QUESTEDGE FICS T: +44 7902 615370 E: cargo@fernholt-example.com

Font styles to use
Serif

Colors

Designer to choose colors to be used in the design.

Requirements
Must have
• Garamond / Times New Roman or similar text in black colour

```html
<!DOCTYPE html>
<html lang="en">
<head>
<meta charset="utf-8">
<title>Fernholt International Ltd – Business Card</title>
<link rel="stylesheet" href="https://fonts.googleapis.com/css2?family=Tinos:wght@700&display=swap">
<style>
  :root {
    --backdrop: #7a7a7a;
    --card: #ffffff;
    --ink: #000000;
    --card-w: 880px;
    --card-h: 501px;
  }
  * { box-sizing: border-box; margin: 0; padding: 0; }
  html, body {
    width: 1071px;
    height: 1200px;
    overflow: hidden;
    background: var(--backdrop);
  }
  .canvas {
    width: 1071px;
    height: 1200px;
    display: flex;
    flex-direction: column;
    align-items: center;
    justify-content: space-evenly;
  }
  .card {
    position: relative;
    width: var(--card-w);
    height: var(--card-h);
    background: var(--card);
    color: var(--ink);
    font-family: "Tinos", "Times New Roman", serif;
    font-weight: 700;
    overflow: hidden;
  }
  .card__bands {
    position: absolute;
    inset: 0;
    width: 100%;
    height: 100%;
  }
  .card__bands polygon { fill: var(--ink); }

  .company {
    position: absolute;
    left: 0;
    right: 0;
    top: 208px;
    text-align: center;
    line-height: 1;
    font-weight: 700;
  }
  .company__name {
    display: block;
    font-size: 40px;
    letter-spacing: 0.5px;
  }
  .company__suffix {
    display: block;
    font-size: 28px;
    margin-top: 2px;
  }

  .holder {
    position: absolute;
    left: 0;
    right: 0;
    top: 180px;
    text-align: center;
    font-size: 37px;
    line-height: 1;
  }
  .contact {
    position: absolute;
    left: 460px;
    top: 384px;
    list-style: none;
    font-size: 18px;
    line-height: 1.25;
  }
</style>
</head>
<body>
  <main class="canvas">
    <section class="card card--front" aria-label="Business card front">
      <svg class="card__bands" viewBox="0 0 337 192" preserveAspectRatio="none" aria-hidden="true">
        <polygon points="0,152 128,152 134,166 0,166"/>
        <polygon points="136,152 154,152 170,172 337,172 337,186 163,186"/>
      </svg>
      <h1 class="company">
        <span class="company__name">FERNHOLT</span>
        <span class="company__suffix">INTERNATIONAL LTD</span>
      </h1>
    </section>

    <section class="card card--back" aria-label="Business card back">
      <svg class="card__bands" viewBox="0 0 337 192" preserveAspectRatio="none" aria-hidden="true">
        <polygon points="0,152 128,152 134,166 0,166"/>
        <polygon points="136,152 154,152 170,172 337,172 337,186 163,186"/>
      </svg>
      <h2 class="holder">MARTIN QUESTEDGE FICS</h2>
      <ul class="contact">
        <li class="contact__phone">+44 7902 615370</li>
        <li class="contact__email">cargo@fernholt-example.com</li>
      </ul>
    </section>
  </main>
</body>
</html>
```